Recherche d'une étiquette pour une bouteille de vin

I need a wine label for a Spanish Ribera del Tormel wine.
The wine already exist burt the label is quiete ugly (see attached)
I've made a firsrt research but I don't like it (pdf attached)

Je cherche a faire une étiquette pur du vin de la Ribera del Tormel.
Le vin existe déjà mais l'étiquette est très moche.
J'ai fais une 1ere recherche mais elle ne me plaît pas (pdf joint)
Updates

Besoin de plus de jours pour examiner

Besoin de quelques jours pour choisir un design

Target Market(s)

Suisse espagne

Industry/Entity Type

Vineyard

Colors

Designer to choose colors to be used in the design.

Requirements
Must have
• Please use black color + 2 pantone color
• Merci d'utiliser le noir + 2 couleur pantone
• Format: 54 x 124mm
Nice to have
• Le logo Ribera del Tormel (joint)

```html
<!DOCTYPE html>
<html lang="es">
<head>
<meta charset="utf-8">
<title>Corvel Aurea – Etiqueta</title>
<link rel="stylesheet" href="https://fonts.googleapis.com/css2?family=Josefin+Sans:wght@300;400;600&family=Oswald:wght@400;500&display=swap">
<style>
  :root {
    --page: #e6e3e8;
    --label-plum: #3b2b46;
    --accent-magenta: #b3426f;
    --accent-deep: #8e3760;
    --ink-white: #f4f1f4;
    --ink-soft: #cfc4d3;
    --ink-blush: #f1dbe5;
  }
  * { margin: 0; padding: 0; box-sizing: border-box; }
  html, body {
    width: 1200px; height: 900px; overflow: hidden;
    background: var(--page);
  }
  .canvas {
    position: relative; width: 1200px; height: 900px;
    display: flex; align-items: center; justify-content: center;
  }
  .wine-label {
    position: relative;
    width: 386px; height: 820px;
    background: var(--label-plum);
    color: var(--ink-white);
    font-family: "Josefin Sans", sans-serif;
    text-align: center;
    overflow: hidden;
  }
  .brand {
    position: absolute; top: 74px; left: 0; right: 0;
    font-weight: 400; font-size: 40px; line-height: 36px;
    letter-spacing: 4px;
  }
  .brand-first { display: block; color: var(--ink-white); }
  .brand-second { display: block; color: var(--accent-magenta); font-weight: 300; }
  .region {
    position: absolute; top: 180px; left: 0; right: 0;
    font-family: "Oswald", sans-serif; font-weight: 400;
    font-size: 20px; letter-spacing: 1px; line-height: 1;
  }
  .appellation {
    position: absolute; top: 204px; left: 0; right: 0;
    font-family: "Oswald", sans-serif; font-size: 9px; letter-spacing: 1px;
    color: var(--ink-soft);
  }
  .vintage {
    position: absolute; top: 258px; left: 0; right: 0;
    font-weight: 300; font-size: 46px; letter-spacing: 2px; line-height: 1;
  }
  .vintage-end { color: var(--accent-magenta); font-weight: 600; }
  .council-mark {
    position: absolute; top: 356px; left: 0; right: 0;
    display: flex; align-items: center; justify-content: center; gap: 6px;
    font-family: "Oswald", sans-serif; font-size: 11px; letter-spacing: 2px;
  }
  .council-square {
    width: 10px; height: 10px; background: var(--ink-white);
  }
  .estate-silhouette {
    position: absolute; left: 118px; width: 140px; top: 610px; height: 82px;
    background: linear-gradient(to bottom, var(--accent-deep), var(--accent-magenta));
  }
  .footer-band {
    position: absolute; left: 0; right: 0; top: 690px; bottom: 0;
    background: var(--accent-magenta);
  }
  .volume {
    position: absolute; top: 704px; left: 0; right: 0;
    font-family: "Oswald", sans-serif; font-size: 13px; letter-spacing: 1px;
  }
  .bottler {
    position: absolute; top: 730px; left: 40px; right: 40px;
    font-size: 8px; line-height: 11px; color: var(--ink-blush);
  }
  .origin {
    position: absolute; top: 778px; left: 0; right: 0;
    font-family: "Oswald", sans-serif; font-weight: 500;
    font-size: 14px; letter-spacing: 1.5px;
  }
</style>
</head>
<body>
<main class="canvas">
  <section class="wine-label">
    <h1 class="brand">
      <span class="brand-first">CORVEL</span>
      <span class="brand-second">AUREA</span>
    </h1>
    <p class="region">RIBERA DEL TORMEL</p>
    <p class="appellation">VIÑEDOS DE ALTURA</p>
    <p class="vintage">20<span class="vintage-end">17</span></p>
    <div class="council-mark"><span class="council-square"></span>VALDORA</div>
    <div class="estate-silhouette" role="img" aria-label="Silhouette of the winery estate building"></div>
    <div class="footer-band"></div>
    <p class="volume">ALC. 14% BY VOL. 750ML</p>
    <p class="bottler">Elaborado y embotellado por Bodegas Corvel Aurea S.L.<br>Valle Alto, 47300 – Castilla – España</p>
    <p class="origin">PRODUCT OF SPAIN</p>
  </section>
</main>
</body>
</html>
```